Popup Nightclub Grand Opening Flyer

We need to design a flyer for the grand opening of an upscale, exclusive nightclub called "Lanternfall". The design needs to be chic and exclusive. The background should be black and the text should primarily be white. We like minimalist designs.

Here is the text for the flyer
-
Velvetrope Atlanta Presents

Lanternfall (LOGO)

A Popup Nightclub Experience
For one night Only

Friday, October 18, 2013
Party begins at 9PM

INVITE ONLY

See invitation for location details
(Velvetrope Atlanta logo)

-
Examples we like

http://cdn2-b.brivelpost.com/sites/default/files/styles/image_content_width/hash/3d/fa/1472093815_4471_flyer.jpg?itok=R8kqWm2z

http://api.plovra.com/files/7Kqq-Tr82XXB3pQzJvmtR5HL2W719E4nbRtC6KLd4HsfM8Y2qTDK-VmjwDoNqLX4QBzTHD9nakRbVx3m-Pfq8htc3MDTWr5p4/2zelSaturdays.jpg

http://quenmar.com/wp-content/uploads/yootheme/widgetkit/gallery/2zel/2zel-gen_vroom4-01.jpg

Hi All, one thing that we are seeing that we don't like is on over emphasis on the phrase "a popup nightclub experience" please don't make this the largest thing on the flyer

Target Market(s)

Target market is 25-35 year olds who are affluent (rich) and like luxury brands

Requirements
Must have
• Dark Background
Nice to have
• Velvetrope Logo on the bottom
Modern text that isn't curvy
Should not have
• Curved text

```html
<!DOCTYPE html>
<html lang="en">
<head>
<meta charset="utf-8">
<title>Lanternfall Nightclub – Velvetrope Atlanta</title>
<link rel="stylesheet" href="https://fonts.googleapis.com/css2?family=Tenor+Sans&family=Questrial&display=swap">
<style>
  :root {
    --ink: #ffffff;
    --ink-soft: #e9e9e9;
    --ink-muted: #bdbdbd;
    --night: #050505;
    --wall-light: #3c3c3c;
    --wall-mid: #1c1c1c;
    --rule: #d8d8d8;
  }
  * { margin: 0; padding: 0; box-sizing: border-box; }
  html, body { width: 927px; height: 1200px; overflow: hidden; background: var(--night); }
  .flyer {
    position: relative;
    width: 927px;
    height: 1200px;
    overflow: hidden;
    color: var(--ink);
    font-family: "Tenor Sans", sans-serif;
  }
  .wall {
    position: absolute;
    inset: 0;
    background:
      radial-gradient(ellipse 62% 48% at 50% 30%, var(--wall-light) 0%, var(--wall-mid) 55%, var(--night) 100%);
  }
  .presenter {
    position: absolute;
    top: 38px;
    left: 0;
    width: 100%;
    text-align: center;
    font-size: 56px;
    letter-spacing: 4.6px;
    font-variant: small-caps;
    white-space: nowrap;
  }
  .club-mark {
    position: absolute;
    top: 178px;
    left: 0;
    width: 100%;
    display: flex;
    flex-direction: column;
    align-items: center;
  }
  .club-mark__dot {
    width: 196px;
    height: 196px;
    border-radius: 50%;
    background: linear-gradient(160deg, #f2f2f2, #9a9a9a);
  }
  .club-mark__name {
    margin-top: 64px;
    font-family: "Questrial", sans-serif;
    font-size: 66px;
    letter-spacing: 10px;
    color: var(--ink-soft);
    line-height: 1;
  }
  .club-mark__kind {
    margin-top: 22px;
    font-family: "Questrial", sans-serif;
    font-size: 38px;
    letter-spacing: 7px;
    color: var(--ink-soft);
    line-height: 1;
  }
  .tagline {
    position: absolute;
    top: 652px;
    left: 0;
    width: 100%;
    text-align: center;
    font-size: 50px;
    line-height: 72px;
    letter-spacing: 5.5px;
    font-variant: small-caps;
    white-space: nowrap;
  }
  .rule {
    position: absolute;
    left: 45px;
    width: 836px;
    height: 2px;
    background: var(--rule);
  }
  .rule--top { top: 907px; }
  .rule--bottom { top: 987px; }
  .details {
    position: absolute;
    top: 922px;
    left: 45px;
    width: 836px;
    height: 54px;
    display: flex;
    align-items: center;
    gap: 13px;
    font-family: "Questrial", sans-serif;
    font-size: 31px;
    letter-spacing: 3.2px;
    white-space: nowrap;
  }
  .details__divider {
    width: 1px;
    height: 54px;
    background: var(--rule);
  }
  .host {
    position: absolute;
    top: 1008px;
    left: 45px;
    width: 836px;
    height: 135px;
    display: flex;
    align-items: center;
  }
  .host__dot {
    width: 128px;
    height: 128px;
    border-radius: 50%;
    background: var(--ink);
    margin-left: 45px;
  }
  .host__divider {
    width: 2px;
    height: 128px;
    background: var(--rule);
    margin-left: 87px;
  }
  .host__name {
    margin-left: 53px;
    font-family: "Questrial", sans-serif;
    color: var(--ink);
    line-height: 1;
    white-space: nowrap;
  }
  .host__name-main {
    display: block;
    font-size: 80px;
    letter-spacing: 2px;
  }
  .host__name-city {
    display: block;
    margin-top: 8px;
    font-size: 32px;
    letter-spacing: 8px;
  }
  .entry-note {
    position: absolute;
    top: 1160px;
    left: 0;
    width: 100%;
    text-align: center;
    font-family: "Questrial", sans-serif;
    font-size: 18px;
    letter-spacing: 3px;
    color: var(--ink-muted);
    white-space: nowrap;
  }
  .entry-note__key { color: var(--ink); }
</style>
</head>
<body>
  <main class="flyer">
    <div class="wall" role="img" aria-label="Dark brick wall texture, softly lit from above"></div>

    <p class="presenter">Velvetrope Atlanta Presents</p>

    <div class="club-mark">
      <div class="club-mark__dot"></div>
      <p class="club-mark__name">LANTERNFALL</p>
      <p class="club-mark__kind">NIGHTCLUB</p>
    </div>

    <p class="tagline">A Popup Nightclub Experience<br>For<br>one night Only</p>

    <div class="rule rule--top"></div>
    <div class="details">
      <span class="details__date">Friday, October 18, 2013</span>
      <span class="details__divider"></span>
      <span class="details__time">Party begins at 9PM</span>
    </div>
    <div class="rule rule--bottom"></div>

    <div class="host">
      <div class="host__dot"></div>
      <div class="host__divider"></div>
      <p class="host__name">
        <span class="host__name-main">VELVETROPE</span>
        <span class="host__name-city">ATLANTA</span>
      </p>
    </div>

    <p class="entry-note"><span class="entry-note__key">INVITE ONLY</span> &nbsp;|&nbsp; See invitation for location details</p>
  </main>
</body>
</html>
```